■依頼目的/概要
電子書籍を出版しますので、
表紙デザイン作成をお願いいたします。

■本のタイトル
ソラトビ!
~金沢発 16才女子高生社長の海外体験記~

<著者>株式会社七海舎 代表取締役社長 柴田遥香
※参考に株式会社七海舎 の社名ロゴを添付します。

■本の内容

「株式会社七海舎」の代表取締役社長である
著者、柴田遥香さんが、
海外で感じた事や、

高校生でありながら起業に至る経緯などを、
JKらしい軽快な文体で本にしました。

※参考に本の原稿を資料として添付します。

高校2年生の海外渡航体験で、
東南アジアのエネルギーを
目の当たりにしたことをきっかけに、

「日本の元気のなさってヤバくない?」
「もっと10代のうちに海外を見ようよ!」
と、心の底から感じました。

その思いを形にすべく、現在は、
10代向け海外留学支援サイト「ソラトビ!」を、
立ち上げ運営しています。サイトはこちらです。

https://soratobi-site.example/profile/
※ソラトビ!ロゴを参考材料として添付します。

■デザイン要望

16才の遥香社長の元気でチャレンジャーな感じを表現したいです。

できれば、
遥香さんの写真を使いたいと思っています。

※遥香さんの写真を材料として添付します。
※株式会社七海舎の会社ロゴ、
および運営サイト「ソラトビ!」のロゴも参考に添付しますので、
使用についてはデザイナーさんにお任せします。

その他の
イラストや写真等素材を使用される場合には、
商用利用可の素材をお願いします。

色合い、デザインレイアウトとも、
デザイナーさんにお任せしたいと思います。

■その他、デザインを考えるのに必要な情報などありましたら、
お答えしますので、遠慮なく聞いて下さい。

※添付資料
・遥香社長の写真
・株式会社七海舎のロゴ画像
・留学サイト「ソラトビ!」のロゴ
・原稿たたき
素晴らしいご提案をいただきありがとうございます。
提案予約のご連絡をいただきましたため、
締切日時を2日だけ延長させていただきます。

引き続き、よろしくお願いいたします。

かなり悩みましたが、
ぱっとみてわかりやすい、
ロゴにインパクトがあった、
パブリックな感じがポイントになりました。

この度はご提案いただきありがとうございました。
たくさんのいい提案があり、選考に本当に迷いました。
ご応募してくださったワーカーのみなさまに感謝いたします。

また依頼することもあるかと思いますので、
その時はよろしくお願いいたします。

```html
<!DOCTYPE html>
<html lang="ja">
<head>
<meta charset="utf-8">
<title>ソラトビ! 表紙</title>
<link href="https://fonts.googleapis.com/css2?family=Dela+Gothic+One&family=M+PLUS+Rounded+1c:wght@700;800;900&family=Yomogi&display=swap" rel="stylesheet">
<style>
:root{
  --sky-top:#cfe9f8;
  --sky-mid:#eef7fc;
  --sky-low:#bfe0f3;
  --navy:#1a3a8c;
  --pink:#e0327d;
  --white:#ffffff;
  --ink:#1d2b4f;
}
*{margin:0;padding:0;box-sizing:border-box}
html,body{width:752px;height:1200px;overflow:hidden;background:var(--white)}
.cover{
  position:relative;width:752px;height:1200px;overflow:hidden;
  background:linear-gradient(180deg,var(--sky-top) 0%,var(--sky-mid) 45%,var(--sky-low) 100%);
  font-family:"M PLUS Rounded 1c",sans-serif;
}
.flight-path{position:absolute;left:40px;top:20px;width:420px;height:110px;z-index:3}
.title{
  position:absolute;left:40px;top:95px;z-index:3;
  font-family:"Dela Gothic One",sans-serif;color:var(--navy);
  line-height:1;letter-spacing:-2px;white-space:nowrap;
}
.title .line1{display:block;font-size:104px}
.title .line2{display:block;font-size:118px;margin-top:6px}
.author{position:absolute;right:28px;top:30px;text-align:center;color:var(--ink);z-index:3}
.author .company,.author .role{font-size:21px;font-weight:800;line-height:1.3}
.author .name{font-size:38px;font-weight:900;margin-top:4px;letter-spacing:2px}
.author .name small{font-size:22px;margin-left:6px}
.character{
  position:absolute;left:395px;top:150px;width:330px;height:1020px;
  background:linear-gradient(180deg,#8a4a3a 0%,#f3d6c4 22%,#ffffff 40%,#3a3f55 68%,#f3d6c4 100%);
  border-radius:160px 160px 60px 60px;opacity:.9;z-index:2;
}
.origin-badge{
  position:absolute;left:100px;top:375px;width:82px;height:82px;border-radius:50%;
  background:var(--pink);color:var(--white);font-size:22px;font-weight:900;line-height:1.1;
  display:flex;flex-direction:column;align-items:center;justify-content:center;
  border:4px solid var(--white);z-index:4;text-align:center;
}
.age{
  position:absolute;left:190px;top:352px;color:var(--pink);z-index:4;
  font-family:"Dela Gothic One",sans-serif;font-size:108px;line-height:1;white-space:nowrap;
  -webkit-text-stroke:5px var(--white);paint-order:stroke fill;
}
.age small{font-size:52px}
.band{position:absolute;font-weight:900;z-index:4;white-space:nowrap}
.band-pink{
  left:25px;top:455px;width:500px;height:82px;background:var(--pink);color:var(--white);
  font-size:58px;line-height:82px;padding-left:20px;transform:skewY(-3deg);
}
.band-white{
  left:40px;top:540px;width:380px;height:80px;background:var(--white);color:var(--pink);
  font-size:64px;line-height:80px;padding-left:18px;transform:skewY(-3deg);
}
.photo{
  position:absolute;left:40px;top:650px;width:370px;height:290px;z-index:4;
  background:linear-gradient(180deg,#8fc3e8 0%,#d9e9f2 40%,#6b4a34 70%,#8c8c8c 100%);
  border:8px solid var(--white);transform:rotate(-3deg);box-shadow:0 4px 10px rgba(0,0,0,.2);
}
.message{
  position:absolute;left:310px;top:975px;width:430px;z-index:4;
  font-family:"Yomogi",cursive;font-size:24px;line-height:1.5;color:var(--ink);
  transform:rotate(-4deg);white-space:nowrap;
}
.message .accent{color:var(--pink)}
</style>
</head>
<body>
<main class="cover">
  <svg class="flight-path" viewBox="0 0 420 110" aria-hidden="true">
    <path d="M110 60 Q240 110 410 90" fill="none" stroke="var(--navy)" stroke-width="4" stroke-dasharray="3 9" stroke-linecap="round"/>
    <g fill="var(--navy)" transform="translate(40 45)">
      <path d="M0 12 L70 12 Q82 14 70 18 L0 18 Z"/>
      <path d="M30 12 L50 -12 L58 -12 L46 12 Z"/>
      <path d="M30 18 L50 38 L58 38 L46 18 Z"/>
      <path d="M2 12 L-6 0 L2 0 L12 12 Z"/>
    </g>
  </svg>

  <h1 class="title"><span class="line1">ソラ</span><span class="line2">トビ!</span></h1>

  <div class="author">
    <p class="company">株式会社七海舎</p>
    <p class="role">代表取締役社長</p>
    <p class="name">柴田 遥香<small>著</small></p>
  </div>

  <div class="character" role="img" aria-label="眼鏡にセーラー服の女子高生が空を指さして跳ねるイラスト"></div>

  <div class="origin-badge"><span>金沢</span><span>発</span></div>
  <p class="age">16<small>才</small></p>

  <p class="band band-pink">女子高生社長の</p>
  <p class="band band-white">海外体験記</p>

  <div class="photo" role="img" aria-label="青空の下の金沢駅鼓門の写真"></div>

  <p class="message">日本の元気のなさってヤバくない?<br>もっと10代のうちに<span class="accent">海外</span>を見ようよ!</p>
</main>
</body>
</html>
```